Tech business card design

We need an amazing business card design for our new business 'Vantry' a marketing tech startup based in Sydney, Australia. We provide an online marketplace for businesses to search and buy advertising media, connect with service providers and learn more about marketing. We wish to communicate 'cool tech', reliability and professionalism and design based around our logo.

Target Market(s)

Business Owners

Contact Information for Business Card

Name
Position
Email Address
Website
Phone Number

Font styles to use
Other font styles liked:
• Avenir & Avenir Next

Colors

Designer to choose colors to be used in the design.

```html
<!DOCTYPE html>
<html lang="en">
<head>
<meta charset="utf-8">
<title>Vantry Business Card</title>
<link href="https://fonts.googleapis.com/css2?family=Open+Sans:wght@400;600;700;800&display=swap" rel="stylesheet">
<style>
  :root {
    --backdrop: #9ecde1;
    --card-stock: #a9c4d0;
    --brand-navy: #233169;
    --ink: #3a3f48;
    --white: #ffffff;
    --soft-white: #dfe4f0;
  }
  * { box-sizing: border-box; margin: 0; padding: 0; }
  html, body {
    width: 1200px;
    height: 1050px;
    overflow: hidden;
    background: var(--backdrop);
    font-family: "Open Sans", sans-serif;
  }
  .canvas { position: relative; width: 1200px; height: 1050px; }
  .card {
    position: absolute;
    top: 74px;
    width: 507px;
    height: 884px;
    background: var(--card-stock);
  }
  .card--front { left: 69px; }
  .card--back { left: 622px; }

  .brand-panel {
    position: absolute;
    left: 53px;
    width: 400px;
    height: 476px;
    background: var(--brand-navy);
    color: var(--white);
    text-align: center;
  }
  .card--front .brand-panel { top: 67px; }
  .card--back .brand-panel { top: 204px; }

  .wordmark {
    position: absolute;
    left: 0; right: 0;
    font-weight: 800;
    font-size: 100px;
    line-height: 1;
    letter-spacing: -2px;
    color: var(--white);
  }
  .card--front .wordmark { top: 86px; }
  .card--back .wordmark { top: 152px; }

  .holder-name {
    position: absolute;
    left: 0; right: 0; top: 370px;
    font-weight: 700;
    font-size: 29px;
    line-height: 1;
  }
  .holder-role {
    position: absolute;
    left: 0; right: 0; top: 409px;
    font-weight: 400;
    font-size: 25px;
    line-height: 1;
    color: var(--soft-white);
  }

  .divider {
    position: absolute;
    left: 139px; top: 332px;
    width: 122px; height: 2px;
    background: var(--soft-white);
  }
  .panel-url {
    position: absolute;
    left: 0; right: 0; top: 386px;
    font-size: 26px;
    letter-spacing: 3px;
    line-height: 1;
  }

  .contact-list {
    position: absolute;
    left: 0; right: 0; top: 634px;
    list-style: none;
    color: var(--ink);
    font-size: 23px;
    line-height: 1;
  }
  .contact-item {
    display: flex;
    justify-content: center;
    align-items: center;
    gap: 8px;
    height: 24px;
    margin-bottom: 15px;
  }
  .contact-item--web { letter-spacing: 2.5px; }
  .contact-icon { width: 22px; height: 22px; fill: none; stroke: var(--brand-navy); stroke-width: 1.6; }
  .contact-icon--solid { fill: var(--brand-navy); stroke: none; }

  .address {
    position: absolute;
    left: 0; right: 0; top: 782px;
    text-align: center;
    font-size: 22px;
    line-height: 30px;
    color: var(--ink);
    font-style: normal;
  }
</style>
</head>
<body>
<main class="canvas">
  <section class="card card--front">
    <div class="brand-panel">
      <div class="wordmark">Vantry</div>
      <p class="holder-name">JOHN SMITH</p>
      <p class="holder-role">Position</p>
    </div>
    <ul class="contact-list">
      <li class="contact-item">
        <svg class="contact-icon" viewBox="0 0 24 24" aria-hidden="true">
          <circle cx="12" cy="12" r="10"/>
          <path d="M9 7c-1 1-1.5 3 0 6s3.5 4.5 5 5l1.5-1.5-2-2-1.2.6c-1-.8-1.8-2-2.3-3.2l1-1L10 8z" fill="#233169" stroke="none"/>
        </svg>
        <span>012-345-6789</span>
      </li>
      <li class="contact-item">
        <svg class="contact-icon contact-icon--solid" viewBox="0 0 24 24" aria-hidden="true">
          <path d="M1 4h22v16H1z"/>
          <path d="M1 4l11 9 11-9M1 20l8-8M23 20l-8-8" stroke="#a9c4d0" stroke-width="1.6" fill="none"/>
        </svg>
        <span>info@vantry.com</span>
      </li>
      <li class="contact-item contact-item--web">
        <svg class="contact-icon" viewBox="0 0 24 24" aria-hidden="true">
          <circle cx="12" cy="12" r="10"/>
          <ellipse cx="12" cy="12" rx="4.5" ry="10"/>
          <path d="M2 12h20M4 7h16M4 17h16"/>
        </svg>
        <span>www.vantry.com</span>
      </li>
    </ul>
    <address class="address">Street name City Name,<br>Zipcode,012345</address>
  </section>

  <section class="card card--back">
    <div class="brand-panel">
      <div class="wordmark">Vantry</div>
      <span class="divider"></span>
      <p class="panel-url">www.vantry.com</p>
    </div>
  </section>
</main>
</body>
</html>
```